Complete the design for cleverhub.assure it is for a company that provides Embedded Insurance.

Design a logo and complete the design for http://cleverhub.assure. website that I have provide. So I need a logo and a design and neaten up the site.
http://dev.cleverhub.assure is B2B website. We target any company that wants to offer an insurance product along with their product or service. For example: Online retailers, freight companies, Retail Brands. This is called embedded insurance, and it is used by car hire, airlines and online retailers. When you pay for your product or service you are offered this type of insurance.
dev.cleverhub.assure

We have a few services
1. Cover: providing insurance cover
2. Claim: processing insurance claims
3. Valuations: Providing ongoing insurance valuations
4. Asset Vault: Providing a personal asset vault to keep assets, valuations and insurance.

Also has the ability to interact via API.

Target Market(s)

It is B2B website. We target any company that wants to offer an insurance product along with their product or service. For example: Online retailers, freight companies, Retail Brands. This is called embedded insurance, and it is used by car hire, airlines and online retailers. When you pay for your product or service you are offered this type of insurance.

Industry/Entity Type

Embedded Insurance.

Coding

Coded - Design and coding required

Number of Pages Required

3 page

Font styles to use
Sans Serif

Colors
0094D4
00A9DD
6FCCEA
C7EBF8
E9F6FB
FFC000
F8CF3A
FAE287
FDF2CF
FEFAEE

Requirements
Must have
• A new logo. Unique photographs
Nice to have
• https://shieldwombat.example/ is a competitor. Also http://dev.cleverhub.example is my existing template in the word press website I have setup which is a guide.

```html
<!DOCTYPE html>
<html lang="en">
<head>
<meta charset="utf-8">
<title>CleverHub — Embedded Insurance</title>
<link rel="stylesheet" href="https://fonts.googleapis.com/css2?family=Roboto+Condensed:wght@400;700&family=Roboto:wght@400;500;700&display=swap">
<style>
:root{
  --brand-blue:#0094D4;
  --brand-sky:#00A9DD;
  --brand-light:#6FCCEA;
  --brand-pale:#C7EBF8;
  --brand-mist:#E9F6FB;
  --gold:#FFC000;
  --gold-soft:#F8CF3A;
  --navy:#06123d;
  --deep:#0a5f86;
  --heading:#0b5a7e;
  --ink:#222;
  --muted:#8a8a8a;
  --white:#fff;
  --footer:#1e1e1e;
}
*{box-sizing:border-box;margin:0;padding:0}
html,body{width:1200px;height:4202px;overflow:hidden}
body{position:relative;font-family:"Roboto",sans-serif;color:var(--ink);background:var(--white)}
.abs{position:absolute}
a{color:inherit;text-decoration:none}

/* header */
.header{position:absolute;top:0;left:0;width:1200px;height:98px;background:var(--white);border-top:3px solid var(--brand-sky)}
.logo{position:absolute;left:147px;top:34px;display:flex;align-items:center;gap:10px;font-size:32px;font-weight:500;color:var(--brand-blue)}
.logo-dot{width:26px;height:26px;border-radius:50%;background:var(--gold)}
.top-btn{position:absolute;top:0;height:36px;width:180px;display:flex;align-items:center;justify-content:center;font-size:13px;font-weight:500;color:#fff}
.top-btn.register{left:694px;background:var(--brand-sky)}
.top-btn.meet{left:874px;background:var(--deep)}
.nav{position:absolute;left:454px;top:63px;display:flex;gap:26px;font-size:12px;color:#333;border-left:3px solid var(--brand-sky);padding-left:6px;line-height:16px}

/* hero */
.hero{position:absolute;top:98px;left:0;width:1200px;height:681px;
  background:radial-gradient(ellipse 700px 120px at 600px 230px,rgba(0,169,221,.55),transparent 70%),
  linear-gradient(180deg,#0b3f8a 0%,#071a55 35%,var(--navy) 100%)}
.hero h1{position:absolute;top:112px;width:1200px;text-align:center;font-family:"Roboto Condensed",sans-serif;font-weight:700;font-size:62px;line-height:72px;color:#fff}
.btn{display:flex;align-items:center;justify-content:center;font-size:13px;font-weight:500;color:#fff;background:var(--deep);border:2px solid var(--brand-sky)}
.hero .btn{position:absolute;left:518px;top:279px;width:162px;height:42px}
.service{position:absolute;top:418px;width:200px;text-align:center;color:#fff}
.service .ring{margin:0 auto;width:164px;height:164px;border-radius:50%;background:#fff;border:10px solid #3a4266;display:flex;align-items:center;justify-content:center}
.service .label{margin-top:20px;font-size:13px;font-weight:500}
.service .chev{margin-top:4px}

/* who we are */
.section-title{position:absolute;width:1200px;text-align:center;font-family:"Roboto Condensed",sans-serif;font-weight:700;font-size:44px;color:var(--heading)}
.subline{position:absolute;top:914px;width:1200px;text-align:center;font-size:15px;color:#222}
.feature{position:absolute;top:973px;width:225px;height:220px;color:#fff;text-align:center;padding-top:22px}
.feature.dark{background:var(--deep)}
.feature.light{background:var(--brand-sky)}
.feature h3{margin-top:14px;font-size:16px;font-weight:500}
.feature p{margin:10px auto 0;width:160px;font-size:11px;line-height:16px}
.feature .more{display:block;margin-top:8px;font-size:11px;font-weight:700;text-decoration:underline}
.slider-arrow{position:absolute;top:1052px}

/* process */
.process-title{top:1396px;line-height:52px}
.step{position:absolute;width:260px;text-align:center}
.step .circle{position:relative;margin:0 auto;width:88px;height:88px;border-radius:50%;background:#fff;border:2px solid #ccc;display:flex;align-items:center;justify-content:center}
.step .badge{position:absolute;top:-8px;right:-10px;width:32px;height:32px;border-radius:50%;background:var(--deep);color:#fff;font-size:16px;font-weight:700;display:flex;align-items:center;justify-content:center}
.step h4{margin-top:14px;font-size:14px;font-weight:500;color:#111}
.step p{margin-top:8px;font-size:11px;line-height:17px;color:#999}

/* plans */
.plan{position:absolute;top:2170px;width:294px;height:343px;background:#fff;box-shadow:0 2px 10px rgba(0,0,0,.12);border-radius:4px 4px 0 0}
.plan .cap{height:41px;background:var(--brand-sky);color:#fff;font-size:20px;display:flex;align-items:center;justify-content:center;border-radius:4px 4px 0 0}
.plan.mid .cap{background:var(--deep)}
.plan .price{margin-top:20px;text-align:center;font-size:25px;font-weight:700;color:#222}
.plan .price small{font-size:12px;font-weight:400;color:#999}
.plan ul{list-style:none;margin:26px 0 0 32px}
.plan li{display:flex;align-items:center;gap:16px;height:34px;font-size:12.5px;color:#555}
.plan .btn{margin:22px 0 0 82px;width:132px;height:38px;font-size:12px;font-weight:700;border:none;border-radius:2px}
.plan.mid .btn{background:var(--brand-sky)}

/* embedded */
.emb-title{position:absolute;left:147px;top:2674px;font-family:"Roboto Condensed",sans-serif;font-weight:700;font-size:44px;line-height:52px;color:#fff}
.emb-copy{position:absolute;left:531px;top:2680px;width:478px;font-size:23px;line-height:30px;color:#fff}
.emb-ticks{position:absolute;left:531px;top:2848px;display:flex;gap:10px;font-size:12px;color:#fff;align-items:center}
.emb-ticks span{display:flex;align-items:center;gap:6px}
.stat{position:absolute;top:2882px;color:#fff;font-family:"Roboto Condensed",sans-serif}
.stat b{display:block;font-size:28px}
.stat span{display:block;font-size:17px;margin-top:2px}
.photo{position:absolute}
.tag-box{position:absolute;left:291px;top:3200px;width:280px;height:61px;background:var(--deep);border:2px solid #fff;color:#fff;font-family:"Roboto Condensed",sans-serif;font-size:13px;font-weight:700;line-height:19px;padding:11px 0 0 50px}

/* news */
.news{position:absolute;top:3454px;width:297px}
.news .pic{height:178px}
.news .date{position:absolute;top:166px;left:14px;height:25px;padding:0 16px;background:var(--gold);color:#1b1b1b;font-size:10px;font-weight:500;display:flex;align-items:center}
.news h5{margin-top:36px;font-size:12.5px;font-weight:700;line-height:18px;color:#111}
.news p{margin-top:6px;font-size:11px;line-height:21px;color:#999}
.news .more{display:block;margin-top:14px;font-size:11px;font-weight:700;color:var(--brand-blue)}

/* footer */
.footer-col{position:absolute;top:3942px;color:#fff}
.footer-col h6{font-size:15px;font-weight:700;margin-bottom:8px}
.footer-col p,.footer-col li{font-size:12px;line-height:25px;color:#ddd;list-style:none}
.contact-line{display:flex;gap:14px;align-items:flex-start}
.email-input{margin-top:2px;width:222px;height:36px;background:#fff;color:#666;font-size:12px;display:flex;align-items:center;padding-left:12px}
.signup{margin-top:11px;width:78px;height:31px;background:var(--brand-sky);color:#fff;font-size:11px;font-weight:500;display:flex;align-items:center;justify-content:center}
.copyright{position:absolute;left:147px;top:4150px;font-size:11px;color:#ddd}
.social{position:absolute;left:930px;top:4148px;display:flex;gap:20px}
.social span{width:18px;height:18px;border-radius:50%;background:#9a9a9a}
</style>
</head>
<body>

<header class="header">
  <div class="logo"><span class="logo-dot"></span>CLEVERHUB</div>
  <a class="top-btn register" href="#">REGISTER / LOGIN</a>
  <a class="top-btn meet" href="#">MEET WITH US</a>
  <nav class="nav"><a>HOME</a><a>SERVICES</a><a>INDUSTRIES</a><a>ABOUT US</a><a>PRICING</a><a>BLOG</a><a>CONTACT US</a><a>CAREER</a></nav>
</header>

<section class="hero" role="img" aria-label="Glowing blue digital horizon with light particles">
  <h1>GENERAL INSURANCE<br>DESIGNED FOR YOU</h1>
  <a class="btn" href="#">MEET WITH US</a>
  <div class="service" style="left:140px"><div class="ring"><svg width="70" height="64" viewBox="0 0 70 64" fill="none" stroke="#0a5f86" stroke-width="2.5"><rect x="4" y="4" width="62" height="42" rx="3"/><path d="M35 46v10M22 58h26"/><circle cx="35" cy="25" r="8"/></svg></div><div class="label">CLEVERHUB COVER</div><svg class="chev" width="16" height="14" viewBox="0 0 16 14" fill="none" stroke="#fff" stroke-width="2.5"><path d="M2 2l6 5 6-5M2 7l6 5 6-5"/></svg></div>
  <div class="service" style="left:379px"><div class="ring"><svg width="70" height="64" viewBox="0 0 70 64" fill="none" stroke="#0a5f86" stroke-width="2.5"><rect x="4" y="4" width="62" height="42" rx="3"/><path d="M35 46v10M22 58h26M14 16h20M14 26h30M14 36h16"/></svg></div><div class="label">CLEVERHUB CLAIMS</div><svg class="chev" width="16" height="14" viewBox="0 0 16 14" fill="none" stroke="#fff" stroke-width="2.5"><path d="M2 2l6 5 6-5M2 7l6 5 6-5"/></svg></div>
  <div class="service" style="left:620px"><div class="ring"><svg width="70" height="64" viewBox="0 0 70 64" fill="none" stroke="#0a5f86" stroke-width="2.5"><rect x="4" y="4" width="62" height="42" rx="3"/><path d="M35 46v10M22 58h26M35 12v20M27 20l8-8 8 8"/></svg></div><div class="label">CLEVERHUB VALUATIONS</div><svg class="chev" width="16" height="14" viewBox="0 0 16 14" fill="none" stroke="#fff" stroke-width="2.5"><path d="M2 2l6 5 6-5M2 7l6 5 6-5"/></svg></div>
  <div class="service" style="left:860px"><div class="ring"><svg width="70" height="64" viewBox="0 0 70 64" fill="none" stroke="#0a5f86" stroke-width="2.5"><rect x="4" y="4" width="62" height="42" rx="3"/><path d="M35 46v10M22 58h26M4 14h62M14 24h18M14 32h26M44 24h12v12H44z"/></svg></div><div class="label">CLEVERHUB ASSET VALET</div><svg class="chev" width="16" height="14" viewBox="0 0 16 14" fill="none" stroke="#fff" stroke-width="2.5"><path d="M2 2l6 5 6-5M2 7l6 5 6-5"/></svg></div>
</section>
<svg class="abs" style="left:0;top:611px" width="140" height="169"><polygon points="0,0 139,168 0,168" fill="#fff"/></svg>

<h2 class="section-title" style="top:838px">WHO WE ARE</h2>
<p class="subline">WE PROVIDE TECHNOLOGY SOLUTIONS TO THE INSURANCE INDUSTRY.</p>
<svg class="slider-arrow" style="left:70px" width="36" height="68" fill="none" stroke="#999" stroke-width="1.5"><path d="M34 2L2 34l32 32"/></svg>
<svg class="slider-arrow" style="left:1094px" width="36" height="68" fill="none" stroke="#999" stroke-width="1.5"><path d="M2 2l32 32L2 66"/></svg>
<div class="feature dark" style="left:143px"><svg width="54" height="50" fill="none" stroke="#fff" stroke-width="2"><path d="M14 22a10 10 0 0 1 4-15 13 13 0 0 1 22 4 9 9 0 0 1 0 11z"/><rect x="20" y="14" width="14" height="14"/><path d="M27 28v10M12 38h30M12 38v6M42 38v6M27 38v6"/></svg><h3>HOSTED CLOUD</h3><p>There are many variations of passages of available but the majority</p><a class="more">LEARN MORE</a></div>
<div class="feature light" style="left:373px"><svg width="54" height="50" fill="none" stroke="#fff" stroke-width="2"><rect x="26" y="2" width="20" height="34"/><path d="M30 10h12M30 18h12M30 26h12"/><circle cx="40" cy="42" r="6"/><path d="M6 36a8 8 0 0 1 14 0h-14zM10 8v16M6 12l4-4 4 4"/></svg><h3>CLOUD INTERFACES</h3><p>There are many variations of passages of available but the majority</p><a class="more">LEARN MORE</a></div>
<div class="feature dark" style="left:603px"><svg width="54" height="50" fill="none" stroke="#fff" stroke-width="2"><rect x="6" y="4" width="42" height="18"/><path d="M14 10h26M14 16h20M22 22v18l6-4 6 8"/></svg><h3>SUBSCRIPTION MODEL</h3><p>There are many variations of passages of available but the majority</p><a class="more">LEARN MORE</a></div>
<div class="feature light" style="left:833px"><svg width="54" height="50" fill="none" stroke="#fff" stroke-width="2"><path d="M8 10l8-6h8v42H8zM30 4h8l8 6v36H30z"/><path d="M14 18h4M14 26h4M36 18h4M36 26h4"/></svg><h3>BESPOKE SOLUTIONS</h3><p>There are many variations of passages of available but the majority</p><a class="more">LEARN MORE</a></div>

<svg class="abs" style="left:0;top:1231px" width="1200" height="832" role="img" aria-label="Pale blue backdrop with faint sketch of a light bulb and business doodles"><polygon points="0,146 1200,0 1200,831 0,684" fill="var(--brand-mist)"/></svg>
<h2 class="section-title process-title">WE DEAL WITH THE ASPECTS OF<br>PROFESSIONAL IT SERVICES</h2>
<svg class="abs" style="left:370px;top:1570px" width="480" height="70" fill="none" stroke="#8a8a8a" stroke-width="1.5" stroke-dasharray="5 4"><path d="M2 20C80 2 160 0 196 40"/><path d="M280 48C350 60 420 30 474 12"/><path d="M188 34l8 6 0-10M468 6l8 4-6 6" stroke-dasharray="none"/></svg>
<div class="step" style="left:131px;top:1537px"><div class="circle"><svg width="48" height="40" fill="none" stroke="#0a5f86" stroke-width="2"><rect x="2" y="2" width="44" height="28"/><path d="M24 30v6M14 38h20M8 8h14v12H8zM26 10h14M26 16h10"/></svg><span class="badge">1</span></div><h4>ADVERTISING AND MARKETING</h4><p>Sed ut perspiciatis unde omnis iste natus error<br>sit voluptatem accusantium doloremque</p></div>
<div class="step" style="left:470px;top:1645px"><div class="circle"><svg width="48" height="40" fill="none" stroke="#0a5f86" stroke-width="2"><rect x="2" y="2" width="44" height="28"/><path d="M24 30v6M14 38h20M18 10l-5 6 5 6M30 10l5 6-5 6M26 8l-4 16"/></svg><span class="badge">2</span></div><h4>WEBSITE DEVELOPMENT</h4><p>Sed ut perspiciatis unde omnis iste natus error<br>sit voluptatem accusantium doloremque</p></div>
<div class="step" style="left:807px;top:1537px"><div class="circle"><svg width="48" height="40" fill="none" stroke="#0a5f86" stroke-width="2"><rect x="16" y="2" width="18" height="36" rx="3"/><path d="M22 14l-3 4 3 4M28 14l3 4-3 4M10 12v16M40 12v16"/></svg><span class="badge">3</span></div><h4>MOBILE APP DEVELOPMENT</h4><p>Sed ut perspiciatis unde omnis iste natus error<br>sit voluptatem accusantium doloremque</p></div>
<a class="btn abs" style="left:518px;top:1848px;width:162px;height:42px" href="#">MEET WITH US</a>

<h2 class="section-title" style="top:2080px">CHOOSE YOUR BEST PLAN</h2>
<div class="plan" style="left:143px"><div class="cap">STANDARD</div><div class="price">$29.99<small>/ per Month*</small></div><ul><li><svg width="12" height="12" fill="none" stroke="#0a5f86" stroke-width="1.6"><circle cx="6" cy="6" r="5"/><path d="M3.5 6l2 2 3-3.5"/></svg>Limited install</li><li><svg width="12" height="12" fill="none" stroke="#0a5f86" stroke-width="1.6"><circle cx="6" cy="6" r="5"/><path d="M3.5 6l2 2 3-3.5"/></svg>Unlimited Download</li><li><svg width="12" height="12" fill="none" stroke="#0a5f86" stroke-width="1.6"><circle cx="6" cy="6" r="5"/><path d="M3.5 6l2 2 3-3.5"/></svg>Free One Year Support</li><li><svg width="12" height="12" fill="none" stroke="#0a5f86" stroke-width="1.6"><circle cx="6" cy="6" r="5"/><path d="M3.5 6l2 2 3-3.5"/></svg>Free 1 5 GB Linux Hosting</li></ul><a class="btn" href="#">CHOOSE PLAN</a></div>
<div class="plan mid" style="left:453px"><div class="cap">STANDARD</div><div class="price">$59.99<small>/ per Month*</small></div><ul><li><svg width="12" height="12" fill="none" stroke="#0a5f86" stroke-width="1.6"><circle cx="6" cy="6" r="5"/><path d="M3.5 6l2 2 3-3.5"/></svg>Limited install</li><li><svg width="12" height="12" fill="none" stroke="#0a5f86" stroke-width="1.6"><circle cx="6" cy="6" r="5"/><path d="M3.5 6l2 2 3-3.5"/></svg>Unlimited Download</li><li><svg width="12" height="12" fill="none" stroke="#0a5f86" stroke-width="1.6"><circle cx="6" cy="6" r="5"/><path d="M3.5 6l2 2 3-3.5"/></svg>Free One Year Support</li><li><svg width="12" height="12" fill="none" stroke="#0a5f86" stroke-width="1.6"><circle cx="6" cy="6" r="5"/><path d="M3.5 6l2 2 3-3.5"/></svg>Free 1 5 GB Linux Hosting</li></ul><a class="btn" href="#">CHOOSE PLAN</a></div>
<div class="plan" style="left:763px"><div class="cap">STANDARD</div><div class="price">$79.99<small>/ per Month*</small></div><ul><li><svg width="12" height="12" fill="none" stroke="#0a5f86" stroke-width="1.6"><circle cx="6" cy="6" r="5"/><path d="M3.5 6l2 2 3-3.5"/></svg>Limited install</li><li><svg width="12" height="12" fill="none" stroke="#0a5f86" stroke-width="1.6"><circle cx="6" cy="6" r="5"/><path d="M3.5 6l2 2 3-3.5"/></svg>Unlimited Download</li><li><svg width="12" height="12" fill="none" stroke="#0a5f86" stroke-width="1.6"><circle cx="6" cy="6" r="5"/><path d="M3.5 6l2 2 3-3.5"/></svg>Free One Year Support</li><li><svg width="12" height="12" fill="none" stroke="#0a5f86" stroke-width="1.6"><circle cx="6" cy="6" r="5"/><path d="M3.5 6l2 2 3-3.5"/></svg>Free 1 5 GB Linux Hosting</li></ul><a class="btn" href="#">CHOOSE PLAN</a></div>

<svg class="abs" style="left:0;top:2556px" width="1200" height="560"><polygon points="0,101 1200,0 1200,560 0,560" fill="var(--deep)"/></svg>
<h2 class="emb-title">EMBEDDED<br>INSURANCE</h2>
<p class="emb-copy">Leveraging your brand to provide insurance to your customers. Giving your customers life long product lifecycle management an added benefit and ensuring product satisfaction security when making a purchase.</p>
<div class="emb-ticks">
  <span><svg width="12" height="12" fill="none" stroke="#FFC000" stroke-width="1.6"><circle cx="6" cy="6" r="5"/><path d="M3.5 6l2 2 3-3.5"/></svg>Warranty management</span>
  <span><svg width="12" height="12" fill="none" stroke="#FFC000" stroke-width="1.6"><circle cx="6" cy="6" r="5"/><path d="M3.5 6l2 2 3-3.5"/></svg>Insurance</span>
  <span><svg width="12" height="12" fill="none" stroke="#FFC000" stroke-width="1.6"><circle cx="6" cy="6" r="5"/><path d="M3.5 6l2 2 3-3.5"/></svg>Life cycle care</span>
  <span><svg width="12" height="12" fill="none" stroke="#FFC000" stroke-width="1.6"><circle cx="6" cy="6" r="5"/><path d="M3.5 6l2 2 3-3.5"/></svg>Upgrades and Updates</span>
</div>
<div class="stat" style="left:143px"><b>100 +</b><span>Registered Brokerages</span></div>
<div class="stat" style="left:403px"><b>8 +</b><span>Policy types</span></div>
<div class="stat" style="left:595px"><b>1000 +</b><span>Insurance policies written</span></div>
<div class="stat" style="left:869px"><b>1000 +</b><span>Happily insured customers</span></div>

<svg class="photo" style="left:0;top:3010px" width="1200" height="272">
  <polygon points="0,0 289,4 289,272 0,272" fill="#b9a28b" role="img" aria-label="Team meeting around an office table"/>
  <polygon points="289,44 598,40 598,272 289,272" fill="#d9d7d3" role="img" aria-label="Hand signing a document"/>
  <polygon points="598,38 910,46 910,272 598,272" fill="#4b5e72" role="img" aria-label="Colleagues reviewing papers together"/>
  <polygon points="910,46 1200,82 1200,272 910,272" fill="#9aa3ad" role="img" aria-label="Smiling team working at laptops"/>
</svg>
<div class="tag-box">MARKETING<br>SOFTWARE LICENSE MANAGEMENT</div>

<h2 class="section-title" style="top:3370px">LATEST NEWS</h2>
<article class="news" style="left:143px"><div class="pic" role="img" aria-label="Business people talking in a bright office" style="background:linear-gradient(135deg,#c7ccd2,#7d8792)"></div><span class="date">APRIL 10, 2021 IT SERVICE</span><h5>KEEP YOUR BUSINESS SAFE ENSURE<br>HIGH AVAILABILITY.</h5><p>Sed ut perspiciatis unde omnis iste natus error sit<br>voluptatem accusantium doloremque</p><a class="more">READ MORE</a></article>
<article class="news" style="left:452px"><div class="pic" role="img" aria-label="Businessman touching a glowing digital chart" style="background:linear-gradient(135deg,#1b3f6e,#0b1d3c)"></div><span class="date">APRIL 10, 2021 IT SERVICE</span><h5>WHAT'S THE HOLDING BACK THE IT<br>SOLUTION INDUSTRY?</h5><p>Sed ut perspiciatis unde omnis iste natus error sit<br>voluptatem accusantium doloremque</p><a class="more">READ MORE</a></article>
<article class="news" style="left:758px"><div class="pic" role="img" aria-label="Business people silhouetted against city towers" style="background:linear-gradient(135deg,#5d7e9c,#1f3447)"></div><span class="date">APRIL 10, 2021 IT SERVICE</span><h5>THIS WEEK'S TOP STORIES ABOUT<br>IT SOLUTION</h5><p>Sed ut perspiciatis unde omnis iste natus error sit<br>voluptatem accusantium doloremque</p><a class="more">READ MORE</a></article>

<svg class="abs" style="left:0;top:3858px" width="1200" height="344"><polygon points="0,56 1200,0 1200,344 0,344" fill="var(--footer)"/></svg>
<div class="footer-col" style="left:147px;width:200px"><h6>COMPANY</h6><p>At Brightwell Systems, we are about technology and dedicated to providing IT solutions for businesses of all sizes.</p></div>
<div class="footer-col" style="left:416px"><h6>LINKS</h6><ul><li>Service</li><li>Portfolio</li><li>Contact us</li><li>Blog Us</li><li>About Us</li></ul></div>
<div class="footer-col" style="left:574px;width:200px"><h6>CONTACT INFO</h6>
  <div class="contact-line"><svg width="12" height="24" viewBox="0 0 12 24" fill="#ddd"><path d="M6 6a4 4 0 0 1 4 4c0 3-4 7-4 7s-4-4-4-7a4 4 0 0 1 4-4z"/></svg><p>48 Harbour Lane<br>Northfield, NC 27000</p></div>
  <div class="contact-line"><svg width="12" height="24" viewBox="0 0 12 24" fill="#ddd"><path d="M2 8l2-2 2 3-1 1a6 6 0 0 0 3 3l1-1 3 2-2 2C6 16 2 12 2 8z"/></svg><p>+000-555-0142</p></div>
  <div class="contact-line"><svg width="12" height="24" viewBox="0 0 12 24" fill="#ddd"><path d="M1 8h10v8H1z"/></svg><p>hello@cleverhub.example</p></div>
</div>
<div class="footer-col" style="left:833px"><h6>EMAIL SIGN UP</h6><div class="email-input">Enter Email</div><div class="signup">SIGN UP</div></div>
<p class="copyright">Copyright © 2024. CleverHub All Right Reserved</p>
<div class="social"><span></span><span></span><span></span><span></span></div>

</body>
</html>
```